Business Card Design Project

I need a business card design for our new logo, please check the logo at the following link:
https://www.filecrate.net/s/q7rtx2pw9kd41m/FernLoop.png
The address on the business card:
Av. Gervásio Tavares 418 sala 207
Barra da Tijuca, Rio de Janeiro, RJ
CEP: 22714-380
Brasil
Phone: +55 21 86347215
e-mail: osvaldo@fernloop.com.br
Updates
Thank you all for sending your designs, we will not provide feedback because there are too many designs, on December 3 we will pick the best design according to our point of view. Please keep posting.
Osvaldo
Industry/Entity Type
Business
Look and feel
Each slider illustrates characteristics of the customer's brand and the style your logo design should communicate.

```html
<!DOCTYPE html>
<html lang="pt-BR">
<head>
<meta charset="utf-8">
<title>FernLoop – Business Card</title>
<link rel="stylesheet" href="https://fonts.googleapis.com/css2?family=Source+Sans+3:wght@400;600;700&display=swap">
<style>
  :root {
    --backdrop: #3a3a3a;
    --card: #ffffff;
    --ink: #1d1d1b;
    --ink-soft: #3c3c3b;
    --accent: #f7c600;
    --radius: 28px;
  }
  * { margin: 0; padding: 0; box-sizing: border-box; }
  html, body {
    width: 1200px; height: 900px; overflow: hidden;
    background: var(--backdrop);
    font-family: "Source Sans 3", Arial, sans-serif;
    color: var(--ink);
  }
  .card {
    position: absolute; top: 308px;
    width: 513px; height: 283px;
    background: var(--card);
    border-radius: var(--radius);
    overflow: hidden;
  }
  .card--front { left: 73px; }
  .card--back { left: 616px; }

  .brand-mark { position: absolute; left: 38px; top: 98px; display: flex; align-items: center; gap: 8px; }
  .brand-mark__dot { width: 18px; height: 18px; border-radius: 50%; background: var(--accent); }
  .brand-mark__name { font-size: 32px; font-weight: 700; line-height: 1; color: var(--ink); letter-spacing: -0.5px; }

  .holder { position: absolute; left: 40px; top: 180px; }
  .holder__name { font-size: 16px; font-weight: 600; line-height: 1.1; }
  .holder__role { font-size: 10px; font-weight: 700; margin-top: 2px; }

  .address {
    position: absolute; left: 40px; top: 218px;
    font-size: 10.5px; line-height: 12.5px; color: var(--ink-soft);
    font-style: normal;
  }
  .divider { position: absolute; left: 207px; top: 219px; width: 1px; height: 41px; background: var(--ink); }
  .contacts {
    position: absolute; left: 222px; top: 218px; list-style: none;
    font-size: 10.5px; line-height: 12.5px; color: var(--ink-soft);
  }
  .contacts li { display: flex; align-items: center; gap: 5px; white-space: nowrap; }
  .contacts svg { width: 10px; height: 10px; fill: var(--accent); flex: none; }

  .illustration { position: absolute; border-radius: 6px; }
  .illustration--front {
    left: 368px; top: 42px; width: 145px; height: 202px;
    background: linear-gradient(170deg, #e9c21a 0%, #3a3a36 30%, var(--ink) 60%);
  }
  .illustration--back {
    left: 0; top: 42px; width: 160px; height: 180px;
    background: linear-gradient(190deg, #e9c21a 0%, #3a3a36 30%, var(--ink) 60%);
  }

  .wordmark {
    position: absolute; left: 180px; top: 100px;
    font-size: 74px; font-weight: 700; line-height: 1; letter-spacing: -1px;
    color: var(--ink); white-space: nowrap;
  }
</style>
</head>
<body>
  <section class="card card--front">
    <div class="brand-mark">
      <span class="brand-mark__dot"></span>
      <span class="brand-mark__name">FernLoop</span>
    </div>

    <div class="holder">
      <p class="holder__name">Osvaldo Ribeiro</p>
      <p class="holder__role">founder and owner</p>
    </div>

    <address class="address">
      Av. Gervásio Tavares 418 sala 207<br>
      Barra da Tijuca, Rio de Janeiro, RJ<br>
      CEP: 22714-380<br>
      Brasil
    </address>

    <span class="divider"></span>

    <ul class="contacts">
      <li>
        <svg viewBox="0 0 10 10"><path d="M1 3c0-1 1-2 2-2h4c1 0 2 1 2 2v1H7V3H3v1H1zM2 5h6l1 4H1z"/></svg>
        +55 21 86347215
      </li>
      <li>
        <svg viewBox="0 0 10 10"><path d="M0 2h10v6H0zM0 2l5 3.5L10 2" stroke="#fff" stroke-width=".8"/></svg>
        osvaldo@fernloop.com.br
      </li>
      <li>
        <svg viewBox="0 0 10 10"><circle cx="5" cy="5" r="4.5"/><path d="M.5 5h9M5 .5v9M2 2.2c2 1.2 4 1.2 6 0M2 7.8c2-1.2 4-1.2 6 0" stroke="#fff" stroke-width=".6" fill="none"/></svg>
        www.fernloop.com.br
      </li>
    </ul>

    <div class="illustration illustration--front" role="img" aria-label="Brand illustration area"></div>
  </section>

  <section class="card card--back">
    <div class="illustration illustration--back" role="img" aria-label="Brand illustration area"></div>
    <p class="wordmark">FernLoop</p>
  </section>
</body>
</html>
```